2018 Mother's Day and Baby Blessing poster

I need a poster Mother's Day and Baby Blessing ceremony for a Jade Petal Celebration at Sydney Kestrel Cove. There is no specification on the design, however the only requirement is to present mother and baby in the poster. I would like the design to be modern, attractive and simple.

Must have:
Date: 13/5/2018 (Sunday)
Time: 2:00pm (1:00pm registration)
Venue: Wirraminta Park, Kestrel Cove
Logo

```html
<!DOCTYPE html>
<html lang="en">
<head>
<meta charset="utf-8">
<title>Mother's Day &amp; Baby Blessing Ceremony</title>
<link href="https://fonts.googleapis.com/css2?family=Oswald:wght@300;400&family=Yellowtail&display=swap" rel="stylesheet">
<style>
  :root {
    --backdrop: #e9e4df;
    --paper: #ffffff;
    --teal: #61b19a;
    --brown: #4a2a14;
    --orange: #f29120;
    --white: #ffffff;
    --ink: #1e1e1e;
  }
  * { margin: 0; padding: 0; box-sizing: border-box; }
  html, body {
    width: 1078px; height: 1200px; overflow: hidden;
    background: var(--backdrop);
  }
  .canvas { position: relative; width: 1078px; height: 1200px; }
  .poster {
    position: absolute; left: 123px; top: 23px;
    width: 800px; height: 1110px;
    background: var(--paper);
    transform: scale(1.04); transform-origin: top left;
    box-shadow: 0 6px 24px rgba(0,0,0,.18);
    overflow: hidden;
  }
  .info-band {
    position: absolute; left: 38px; top: 0;
    width: 173px; height: 709px;
    background: var(--teal);
    color: var(--white);
    font-family: "Oswald", sans-serif;
    font-weight: 300;
  }
  .lotus-art {
    position: absolute; left: 22px; top: 62px;
    width: 128px; height: 118px;
    border-radius: 50%;
    background: radial-gradient(circle at 50% 45%, #f7b9cc 0%, #f9d7e2 45%, rgba(255,255,255,.5) 70%, rgba(255,255,255,0) 72%);
  }
  .info-block { position: absolute; left: 14px; width: 139px; }
  .info-block.date { top: 378px; }
  .info-block.time { top: 488px; }
  .info-block.venue { top: 592px; }
  .info-label {
    display: flex; align-items: center; gap: 5px;
    font-weight: 400; font-size: 21px; line-height: 1;
    padding-bottom: 5px;
    border-bottom: 1px solid rgba(255,255,255,.85);
    letter-spacing: .2px;
  }
  .info-label svg { width: 20px; height: 20px; flex: none; }
  .info-value { font-size: 22px; line-height: 1.4; margin-top: 4px; }
  .info-value.venue-lines { font-size: 21px; line-height: 1.45; }
  .info-note { font-size: 15px; line-height: 1.2; }
  .wreath-art {
    position: absolute; left: 222px; top: 48px;
    width: 560px; height: 560px; border-radius: 50%;
    background: radial-gradient(circle, rgba(255,255,255,0) 54%, #dcefcf 60%, #cfe9c0 66%, rgba(255,255,255,0) 73%);
  }
  .title {
    position: absolute; left: 240px; top: 170px; width: 520px;
    text-align: center;
    font-family: "Yellowtail", cursive;
    font-weight: 400;
    color: var(--brown);
  }
  .title .line { display: block; font-size: 72px; line-height: 1; white-space: nowrap; }
  .title .amp { display: block; font-size: 58px; line-height: 1.05; margin: 4px 0 10px; }
  .ceremony {
    position: absolute; left: 380px; top: 438px;
    width: 276px; height: 80px;
    background: var(--orange);
    transform: rotate(-2deg);
    color: var(--white);
    font-family: "Yellowtail", cursive;
    font-size: 58px; line-height: 80px; text-align: center;
    white-space: nowrap;
  }
  .family-photo {
    position: absolute; left: 340px; top: 598px;
    width: 460px; height: 512px;
    background:
      radial-gradient(ellipse at 68% 30%, #8a4a2a 0%, #a55f3a 22%, rgba(165,95,58,0) 48%),
      radial-gradient(ellipse at 28% 45%, #f5d4c2 0%, #eec0a8 30%, rgba(238,192,168,0) 60%),
      linear-gradient(160deg, #ffffff 0%, #f3e4dc 45%, #e6c2ac 100%);
  }
  .brand {
    position: absolute; left: 38px; top: 880px;
    width: 280px;
    display: flex; align-items: center; gap: 14px;
    font-family: "Oswald", sans-serif; font-weight: 400;
    font-size: 34px; color: var(--ink); line-height: 1.15;
  }
  .brand-dot {
    width: 44px; height: 44px; border-radius: 50%;
    background: var(--orange); flex: none;
  }
</style>
</head>
<body>
<div class="canvas">
  <div class="poster">
    <aside class="info-band">
      <div class="lotus-art" role="img" aria-label="Pink lotus flower illustration"></div>

      <div class="info-block date">
        <div class="info-label">
          <svg viewBox="0 0 20 20" fill="none" stroke="#fff" stroke-width="1.6"><rect x="2" y="4" width="16" height="14" rx="1.5"/><line x1="2" y1="8" x2="18" y2="8"/><line x1="6" y1="2" x2="6" y2="5"/><line x1="14" y1="2" x2="14" y2="5"/></svg>
          DATE
        </div>
        <div class="info-value">13/5/2018</div>
        <div class="info-note">(Sunday)</div>
      </div>

      <div class="info-block time">
        <div class="info-label">
          <svg viewBox="0 0 20 20" fill="none" stroke="#fff" stroke-width="1.8"><circle cx="10" cy="10" r="8"/><polyline points="10,5 10,10 14,10"/></svg>
          TIME
        </div>
        <div class="info-value">2:00 pm</div>
        <div class="info-note">(1:00 pm registration)</div>
      </div>

      <div class="info-block venue">
        <div class="info-label">
          <svg viewBox="0 0 20 20" fill="none" stroke="#fff" stroke-width="1.8"><path d="M10 17s-5-5-5-9a5 5 0 0 1 10 0c0 4-5 9-5 9z"/><circle cx="10" cy="8" r="1.8"/><path d="M3 18h14"/></svg>
          VENUE
        </div>
        <div class="info-value venue-lines">Wirraminta Park,<br>Kestrel Cove</div>
      </div>
    </aside>

    <div class="wreath-art" role="img" aria-label="Floral wreath of green leaves and red blossoms"></div>

    <h1 class="title">
      <span class="line">Mother's Day</span>
      <span class="amp">&amp;</span>
      <span class="line">Baby Blessing</span>
    </h1>
    <div class="ceremony">Ceremony</div>

    <div class="family-photo" role="img" aria-label="Photograph of a mother kissing her smiling baby"></div>

    <div class="brand">
      <span class="brand-dot"></span>
      <span>Jade Petal<br>Celebration</span>
    </div>
  </div>
</div>
</body>
</html>
```